We need a business card design for a Dubai based company .

We need a business card for a Dubai based company called "Zernova Smoking Requisites Trading LLC". We mainly import Flavoured Tobacco products and Charcoal which is used for smoking in a Hookah/Shisha and distribute to the wholesalers and retailers. Logo file is attached herewith.

```html
<!DOCTYPE html>
<html lang="en">
<head>
<meta charset="utf-8">
<title>Zernova Smoking Requisites Trading LLC – Business Card</title>
<link rel="stylesheet" href="https://fonts.googleapis.com/css2?family=Michroma&family=Jura:wght@400;500&display=swap">
<style>
  :root {
    --stage: #d9d6d3;
    --card-white: #ffffff;
    --card-black: #060607;
    --brand-red: #e23a3c;
    --ink: #1b1b1b;
    --paper-ink: #f4f4f4;
    --shadow: 0 18px 40px rgba(0, 0, 0, 0.22);
  }
  * { box-sizing: border-box; margin: 0; padding: 0; }
  html, body {
    width: 1200px;
    height: 800px;
    overflow: hidden;
    background: var(--stage);
  }
  .stage {
    width: 1200px;
    height: 800px;
    display: flex;
    align-items: center;
    justify-content: center;
    gap: 40px;
  }
  .card {
    position: relative;
    width: 540px;
    height: 310px;
    border-radius: 26px;
    box-shadow: var(--shadow);
    overflow: hidden;
  }
  .card--front { background: var(--card-white); }
  .card--back {
    background: var(--card-black);
    display: flex;
    align-items: center;
    justify-content: center;
  }

  /* Company name block */
  .brand {
    display: flex;
    align-items: center;
    gap: 12px;
  }
  .brand__square {
    flex: none;
    background: var(--brand-red);
  }
  .brand__name {
    font-family: "Jura", sans-serif;
    font-weight: 500;
    line-height: 1.25;
  }

  .card--front .brand {
    position: absolute;
    left: 34px;
    top: 50%;
    transform: translateY(-50%);
    width: 230px;
  }
  .card--front .brand__square { width: 12px; height: 12px; }
  .card--front .brand__name {
    font-size: 18px;
    color: var(--ink);
  }

  .card--back .brand { width: 400px; }
  .card--back .brand__square { width: 16px; height: 16px; }
  .card--back .brand__name {
    font-size: 28px;
    color: var(--paper-ink);
  }

  /* Holder */
  .holder {
    position: absolute;
    left: 300px;
    top: 44px;
  }
  .holder__name {
    font-family: "Michroma", sans-serif;
    font-size: 17px;
    color: var(--brand-red);
    letter-spacing: 0.02em;
  }
  .holder__title {
    font-family: "Jura", sans-serif;
    font-style: italic;
    font-size: 13px;
    color: var(--ink);
    margin-top: 2px;
    margin-left: 14px;
  }

  /* Contacts */
  .contacts {
    position: absolute;
    left: 300px;
    top: 112px;
    list-style: none;
    display: flex;
    flex-direction: column;
    gap: 9px;
  }
  .contacts__item {
    display: flex;
    align-items: center;
    gap: 11px;
    font-family: "Jura", sans-serif;
    font-weight: 500;
    font-size: 14px;
    color: var(--ink);
    letter-spacing: 0.04em;
  }
  .contacts__icon {
    width: 22px;
    height: 22px;
    border-radius: 50%;
    background: var(--brand-red);
    display: flex;
    align-items: center;
    justify-content: center;
    flex: none;
  }
  .contacts__icon svg { width: 12px; height: 12px; }
</style>
</head>
<body>
<main class="stage">

  <section class="card card--front" aria-label="Business card front">
    <div class="brand">
      <span class="brand__square"></span>
      <span class="brand__name">Zernova Smoking Requisites Trading LLC</span>
    </div>

    <div class="holder">
      <p class="holder__name">Name</p>
      <p class="holder__title">Job title</p>
    </div>

    <ul class="contacts">
      <li class="contacts__item">
        <span class="contacts__icon">
          <svg viewBox="0 0 24 24" fill="#fff"><path d="M6.6 10.8c1.4 2.8 3.8 5.2 6.6 6.6l2.2-2.2c.3-.3.7-.4 1-.2 1.1.4 2.3.6 3.6.6.6 0 1 .4 1 1V20c0 .6-.4 1-1 1C10.6 21 3 13.4 3 4c0-.6.4-1 1-1h3.5c.6 0 1 .4 1 1 0 1.3.2 2.5.6 3.6.1.3 0 .7-.2 1l-2.3 2.2z"/></svg>
        </span>
        00 000 0000
      </li>
      <li class="contacts__item">
        <span class="contacts__icon">
          <svg viewBox="0 0 24 24" fill="#fff"><rect x="7" y="2" width="10" height="20" rx="2"/></svg>
        </span>
        00 000 0000
      </li>
      <li class="contacts__item">
        <span class="contacts__icon">
          <svg viewBox="0 0 24 24" fill="none" stroke="#fff" stroke-width="2"><rect x="3" y="6" width="18" height="12" fill="#fff" stroke="none"/><path d="M3 6l9 7 9-7" stroke="#e23a3c"/></svg>
        </span>
        adress@adress.com
      </li>
      <li class="contacts__item">
        <span class="contacts__icon">
          <svg viewBox="0 0 24 24" fill="#fff"><path d="M12 3l9 8h-3v9h-4v-6h-4v6H6v-9H3z"/></svg>
        </span>
        adress
      </li>
      <li class="contacts__item">
        <span class="contacts__icon">
          <svg viewBox="0 0 24 24" fill="none" stroke="#fff" stroke-width="1.8"><circle cx="12" cy="12" r="9"/><ellipse cx="12" cy="12" rx="4" ry="9"/><path d="M3 12h18M5 7h14M5 17h14"/></svg>
        </span>
        www.website.com
      </li>
    </ul>
  </section>

  <section class="card card--back" aria-label="Business card back">
    <div class="brand">
      <span class="brand__square"></span>
      <span class="brand__name">Zernova Smoking Requisites Trading LLC</span>
    </div>
  </section>

</main>
</body>
</html>
```